依頼詳細
<デザインイメージ>
・ラグジュアリー/高級なイメージ
・VIPのように扱われている
・希少な会に招待されている
記載項目
最低限記載項目:キャッチコピーや見出し/講演タイトル/日時/場所
※講演タイトル/日時/場所については、添付ファイルに記載しています。
※これを使って下さいという素材は特に決まっていません。
サイズ
A4
ページ数
片面
希望イメージ
• +5 0 +5
• シンプル
複雑
• 単色
カラフル
• 暗い
明るい
• 日常
高級
• 遊び心
厳粛
• 未来的
伝統的
• 女性的
男性的
希望する色
黄・オレンジ系、グレー系
納品ファイル
• 高解像度JPG (.jpg)
• イラストレーター形式 (.ai)
• フォトショップ形式 (.psd)
• PNG形式 (.png)
補足説明
依頼公開後の追記内容
<追記>

・講演の内容/テーマ
・講演のスケジュール
・会場について
・チケットの料金
・お申し込み方法
・お問い合わせ先

こちらについては
裏面に記載しております。

チラシ作品として非常に完成度が高かった事に加えて、内容も洗練されていたことが決め手となりました。

この度は、誠に多くのミルダー様にご提案をいただきましたことを、心から感謝いたします。皆様のご提案のクオリティがどれも高く選定にとても悩みました。

この度選定できなかったミルダー様にも、ご縁次第で、また直接ご依頼をさせていただきたいと思っておりますので、今後ともどうぞよろしくお願いいたします。

```html
<!DOCTYPE html>
<html lang="ja">
<head>
<meta charset="utf-8">
<title>ビリオネアの授業 来日講演</title>
<link href="https://fonts.googleapis.com/css2?family=Noto+Sans+JP:wght@500;700;900&family=Noto+Serif+JP:wght@700;900&family=Cinzel:wght@700&display=swap" rel="stylesheet">
<style>
  :root {
    --ink: #0d0d0d;
    --white: #ffffff;
    --red: #d8141a;
    --gray-dark: #3a3a3a;
    --gray-light: #e9e9e9;
    --gold-deep: #3a1e08;
    --gold-mid: #9a5a1c;
    --gold-bright: #f2b45a;
  }
  * { margin: 0; padding: 0; box-sizing: border-box; }
  html, body { width: 867px; height: 1200px; overflow: hidden; background: var(--white); }
  .flyer { position: relative; width: 867px; height: 1200px; overflow: hidden; background: var(--white); font-family: "Noto Sans JP", sans-serif; }

  .header-band {
    position: absolute; left: 0; top: 0; width: 867px; height: 100px;
    background: linear-gradient(90deg, #000 0%, #000 55%, #2a2a2a 100%);
  }
  .speaker-photo {
    position: absolute; right: 0; top: 0; width: 300px; height: 260px;
    background: radial-gradient(ellipse at 60% 40%, #8a8580 0%, #3e3b38 50%, #111 100%);
  }
  .event-label {
    position: absolute; left: 18px; top: 8px; color: var(--white);
    font-weight: 900; font-size: 30px; letter-spacing: 1px;
  }
  .event-label .year { color: var(--white); font-size: 22px; margin-right: 6px; }
  .event-label .tag { color: var(--red); }
  .event-english {
    position: absolute; left: 0; width: 700px; top: 52px; text-align: center;
    font-family: "Cinzel", serif; font-size: 34px; color: var(--white); letter-spacing: 1px;
  }

  .title-band {
    position: absolute; left: 0; top: 100px; width: 867px; height: 165px;
    background: linear-gradient(180deg, rgba(255,255,255,0.95) 0%, rgba(220,220,220,0.9) 100%);
  }
  .title-main {
    position: absolute; left: 0; top: 92px; width: 867px; text-align: center;
    font-weight: 900; font-size: 168px; line-height: 180px; color: var(--white);
    -webkit-text-stroke: 6px var(--ink); paint-order: stroke fill;
    letter-spacing: -4px; transform: scaleY(0.95);
  }
  .title-particle {
    position: absolute; left: 0; top: 262px; width: 867px; text-align: center;
    font-family: "Noto Serif JP", serif; font-weight: 900; font-size: 80px; line-height: 90px; color: var(--ink);
  }
  .title-sub {
    position: absolute; left: 0; top: 352px; width: 867px; text-align: center;
    font-family: "Noto Serif JP", serif; font-weight: 900; font-size: 96px; line-height: 100px; color: var(--ink);
    letter-spacing: 8px;
  }
  .catchcopy {
    position: absolute; left: 0; top: 462px; width: 867px; text-align: center;
    font-family: "Noto Serif JP", serif; font-weight: 900; color: var(--red);
    font-size: 76px; line-height: 90px; white-space: nowrap;
  }
  .catchcopy small { font-size: 34px; vertical-align: 30px; }

  .venue-photo {
    position: absolute; left: 0; top: 565px; width: 867px; height: 635px;
    background:
      radial-gradient(ellipse at 50% 20%, var(--gold-bright) 0%, var(--gold-mid) 35%, transparent 70%),
      radial-gradient(ellipse at 50% 85%, #c9802e 0%, var(--gold-deep) 60%, #120803 100%);
  }

  .info-box {
    position: absolute; left: 160px; top: 735px; width: 614px; height: 265px;
    background: rgba(255,255,255,0.22);
  }
  .info-date {
    position: absolute; left: 185px; top: 752px; color: var(--white);
    font-weight: 900; font-size: 48px; line-height: 60px; white-space: nowrap;
  }
  .info-date .bracket { font-size: 30px; vertical-align: 8px; margin-right: 12px; }
  .info-date .weekday { font-size: 28px; }
  .info-time {
    position: absolute; left: 210px; top: 820px; color: var(--white);
    font-weight: 700; font-size: 30px; white-space: nowrap;
  }
  .info-time .doors { font-size: 20px; }
  .info-place {
    position: absolute; left: 185px; top: 868px; color: var(--white);
    font-weight: 900; font-size: 36px; white-space: nowrap;
  }
  .info-place .bracket { font-size: 26px; margin-right: 8px; }
  .info-station {
    position: absolute; left: 440px; top: 925px; color: var(--white);
    font-weight: 700; font-size: 26px; white-space: nowrap;
  }
  .info-lines {
    position: absolute; right: 95px; top: 970px; color: var(--white);
    font-weight: 700; font-size: 22px; white-space: nowrap;
  }
</style>
</head>
<body>
<main class="flyer">
  <div class="header-band"></div>
  <div class="speaker-photo" role="img" aria-label="講演者の肖像写真"></div>
  <p class="event-label"><span class="year">2018</span><span class="tag">来日講演</span></p>
  <p class="event-english">BILLIONAIRE</p>

  <div class="title-band"></div>
  <h1 class="title-main">ビリオネア</h1>
  <p class="title-particle">の</p>
  <p class="title-sub">授業</p>
  <p class="catchcopy">成功<small>刺激</small>＝億万<small>長者</small></p>

  <div class="venue-photo" role="img" aria-label="金色に照らされた円形の豪華な室内の写真"></div>
  <div class="info-box"></div>
  <p class="info-date"><span class="bracket">【日時】</span>９・１７<span class="weekday">（月・祝）</span></p>
  <p class="info-time">13：00～19：00<span class="doors">／会場12：00</span></p>
  <p class="info-place"><span class="bracket">【場所】</span>浪花中央会館</p>
  <p class="info-station">«北浜橋駅　5分»</p>
  <p class="info-lines">地下鉄中央筋線／浪速電鉄本線</p>
</main>
</body>
</html>
```